Wine Radio Show web re-design

We need new website look for an unconventional, nationally-syndicated WINE RADIO show. Show is fun, hip, witty and covers all wine lifestyle topics. We are redesigning logo and looking for a redesign of our wordpress site that hosts all our audio podcasts, and the site design needs to leverage and maximize these podcasts. Do NOT use the logo currently on the website. The site is corklantern.com, please see more info on the attached.

Do NOT use the logo currently on the website. Please just typeset the name "Cork Lantern Radio".
Updates

Please do NOT use the logo from the current website. Please just use type (to match theme/deisgn) "Cork Lantern Radio". Thank you.

Hello Designers, Thank you for working on this project. A piece of feedback overall is that we'd like much less image/masthead space in general (the photos and images at the top). We'd like the navigation and the latest Cork Lantern podcast to be above the fold. Most of the wine imagery/scenery shots can be minimalized/drastically reduced/eliminated, to allow more room for the different sections. Hope that makes sense, and again, thank you for working on this!! Marla

Target Market(s)

Wine lovers and wine industry professionals, probably 30+ years old

Industry/Entity Type

Radio

Font styles to use
Serif
Sans Serif
Decorative
Other font styles liked:
• Modern retro fonts

Requirements
Must have
• Must keep current content of site:
http://corklanternradio.com/podcast/
Feature podcasts prominently.
Do NOT use the logo currently on the website.
Nice to have
• Graphics to consider incorporating:
• WINE: Grapes, wine glasses, wine bottles, wine pouring, corkscrews, grapevines, vineyards
• RADIO symbols: soundwaves, antenna, radio icon, Podcast symbols, microphone
Should not have
• Do NOT use current logo - just use type.

```html
<!DOCTYPE html>
<html lang="en">
<head>
<meta charset="utf-8">
<title>Cork Lantern Radio</title>
<link rel="stylesheet" href="https://fonts.googleapis.com/css2?family=Cinzel:wght@500&family=Courier+Prime:wght@700&family=IM+Fell+English&family=Open+Sans:wght@400;600&family=Raleway:wght@400;500&display=swap">
<style>
:root{
  --page:#f1efea;
  --panel:#e9e5d8;
  --paper:#f6f3ea;
  --wine:#6e1a2c;
  --wine-text:#7a1f33;
  --gold:#a88a3c;
  --gold-dark:#9a7314;
  --ink:#2b2420;
  --body:#3c3531;
  --muted:#8a8275;
  --rule:#cfc8b4;
  --nav-text:#8f8a80;
}
*{box-sizing:border-box;margin:0;padding:0}
html,body{width:761px;height:1200px;overflow:hidden}
body{background:var(--page);font-family:"Open Sans",sans-serif;color:var(--body);position:relative}
.abs{position:absolute}
.brand{left:72px;top:18px}
.brand-name{font-family:"Courier Prime",monospace;font-weight:700;font-size:15px;color:var(--ink);letter-spacing:1px;display:flex;align-items:center;gap:6px}
.brand-mark{width:10px;height:10px;background:var(--ink)}
.brand-tag{font-family:"Courier Prime",monospace;font-weight:700;font-size:8px;color:var(--ink);margin-left:16px;margin-top:2px}
.social{left:580px;top:23px;display:flex;gap:6px}
.social span{width:19px;height:19px;border-radius:50%;background:#c88a1e;display:block}
.nav{left:63px;top:62px;width:635px;height:31px;background:#fff;display:flex;align-items:center;padding-left:13px;font-family:"Raleway",sans-serif;font-size:9.6px;color:var(--nav-text);box-shadow:0 1px 2px rgba(0,0,0,.15)}
.nav a{text-decoration:none;color:inherit;display:flex;align-items:center}
.nav a+a::before{content:"✣";color:var(--gold);font-size:9px;margin:0 5px 0 8px}
.nav .active{background:var(--gold-dark);color:#fff;padding:3px 9px;font-weight:500}
.hero{left:63px;top:93px;width:635px;height:207px;background:linear-gradient(180deg,#6b5a2e 0%,#c9a24a 40%,#8a6a25 70%,#3a2a18 100%)}
.hero-caption{left:63px;top:270px;width:635px;height:30px;background:linear-gradient(90deg,rgba(20,12,8,.75),rgba(20,12,8,.55));font-family:"Cinzel",serif;font-size:19px;color:#f4ead2;padding-left:18px;line-height:30px;letter-spacing:1.5px}
.main{left:63px;top:300px;width:635px;height:862px;background:var(--panel);box-shadow:0 1px 3px rgba(0,0,0,.12)}
.title{left:77px;top:324px;font-family:"Raleway",sans-serif;font-size:21px;color:var(--ink)}
.title em{font-style:normal;color:var(--wine)}
.title-rule{left:76px;top:355px;width:398px;height:2px;background:var(--gold)}
.feature-photo{left:76px;top:369px;width:397px;height:195px;border:3px solid #fff;background:linear-gradient(180deg,#a8823a 0%,#e2c472 40%,#9a7a32 70%,#4a3a1c 100%);box-shadow:0 0 2px rgba(0,0,0,.2)}
.intro{left:76px;top:575px;width:400px;font-size:8.6px;line-height:12.8px}
.like-row{left:76px;top:672px;display:flex;align-items:center;gap:5px;font-size:7px;color:var(--ink)}
.like-btn{border:1px solid #c9cbd3;background:#eef0f5;color:#3b5488;padding:1px 4px;font-size:7px}
.like-sq{width:7px;height:7px;background:#3b5488}
.tags{left:76px;top:690px;font-size:7.8px;color:var(--muted)}
.tags b{color:var(--wine-text)}
.rule{height:1px;background:var(--rule)}
.h2{font-family:"Raleway",sans-serif;font-size:13.5px;color:var(--ink)}
.bullets{left:76px;top:767px;list-style:none;font-family:"Raleway",sans-serif;font-size:9.8px;color:var(--wine-text)}
.bullets li{height:19.3px;display:flex;align-items:center}
.bullets li::before{content:"";width:4px;height:4px;background:#d8961e;transform:rotate(45deg);margin:0 8px 0 2px}
.btn{left:76px;top:874px;width:105px;height:23px;background:var(--wine);color:#fff;font-family:"Raleway",sans-serif;font-size:9.6px;display:flex;align-items:center;justify-content:center}
.sub{font-family:"Raleway",sans-serif;font-size:12px;color:var(--ink)}
.copy{left:76px;top:940px;width:400px;font-size:8.6px;line-height:12.8px}
.copy a{color:var(--wine-text);text-decoration:none}
.card{left:76px;top:1027px;width:397px;height:73px;background:var(--paper);border-radius:4px;border:1px solid #fff}
.avatar{left:11px;top:10px;width:55px;height:42px;background:linear-gradient(135deg,#b08a60,#6a8a4a);border:2px solid #fff}
.card-name{left:88px;top:6px;font-family:"IM Fell English",serif;font-size:13px;color:var(--wine)}
.card-date{right:12px;top:10px;font-size:8px;color:var(--wine-text)}
.card-rule{left:88px;top:24px;width:297px;height:1px;background:var(--rule)}
.card-text{left:88px;top:32px;width:300px;font-size:7.4px;line-height:11px;color:var(--ink)}
.card-more{right:12px;top:57px;font-size:7.6px;color:var(--wine-text)}
.foot-rule{left:63px;top:1128px;width:635px}
.foot{top:1141px;font-size:7.6px;color:var(--muted)}
.box{left:489px;width:195px;background:var(--paper);border:1px solid #d9d1bb;outline:1px solid #d9d1bb;outline-offset:-5px}
.box-head{position:absolute;left:15px;top:6px;font-family:"IM Fell English",serif;font-size:14px;color:#5a4a3a}
.box-rule{position:absolute;left:15px;top:27px;width:125px;height:1px;background:var(--rule)}
.box-art{position:absolute;right:10px;top:-6px;width:48px;height:40px;background:linear-gradient(180deg,#d8d2c0,#8a8070);opacity:.7}
.blog-text{position:absolute;left:15px;top:38px;width:170px;font-family:Arial,sans-serif;font-size:8.6px;line-height:15.2px;color:#4a403a}
.search-field{position:absolute;left:15px;top:33px;width:139px;height:18px;background:#e8e2d0;border:1px solid #cfc6ae}
.search-btn{position:absolute;left:161px;top:32px;width:20px;height:20px;background:#fff;border:1px solid #cfc6ae;display:flex;align-items:center;justify-content:center}
.fb{left:489px;top:582px;width:195px;height:162px;background:#fff;border:1px solid #c3c6cf}
.fb-title{position:absolute;left:4px;top:5px;font-size:9.6px;font-weight:600;color:#3b5488}
.fb-title small{font-size:7px;font-weight:400}
.fb-like{position:absolute;left:4px;top:22px}
.fb-count{position:absolute;left:12px;top:43px;font-size:6.6px;color:#333}
.fans{position:absolute;left:12px;top:55px;display:grid;grid-template-columns:repeat(5,34.5px);row-gap:3px}
.fan{display:flex;flex-direction:column;align-items:center;font-size:5.6px;color:#3b5488}
.fan i{width:31px;height:31px;display:block;margin-bottom:2px}
.fb-foot{position:absolute;left:0;bottom:0;width:100%;height:12px;border-top:1px solid #d8dbe2;font-size:5.8px;color:#6a7896;padding:2px 0 0 6px;display:flex;gap:4px;align-items:center}
.archive{position:absolute;left:15px;top:37px;display:grid;grid-template-columns:88px 90px;font-family:Arial,sans-serif;font-size:7.8px;line-height:14px;color:#6a6058}
.archive b{color:var(--wine)}
.more{position:absolute;left:15px;top:121px;font-family:Arial,sans-serif;font-weight:bold;font-size:7.8px;color:var(--wine)}
.ep-title{position:absolute;left:15px;top:40px;width:175px;font-size:8.6px;line-height:12.6px;color:var(--ink)}
.ep-text{position:absolute;left:15px;top:74px;width:175px;font-size:8px;line-height:12.6px;color:var(--muted)}
.watch{position:absolute;left:17px;top:136px;display:flex;align-items:center;gap:8px;font-size:8.6px;color:var(--wine)}
</style>
</head>
<body>

<header>
  <div class="abs brand">
    <div class="brand-name"><span class="brand-mark"></span>Cork Lantern Radio</div>
    <div class="brand-tag">Drink And play with us</div>
  </div>
  <div class="abs social" aria-label="Social links"><span></span><span></span><span></span><span></span><span></span></div>
  <nav class="abs nav">
    <a class="active">Home</a><a>Episode Achives</a><a>Uncorked</a><a>About the Show</a><a>About the Host</a><a>On the Air</a><a>Blog</a><a>Store</a><a>Contact</a>
  </nav>
</header>

<div class="abs hero" role="img" aria-label="Wine bottles, glasses and barrels in front of a sunset vineyard"></div>
<div class="abs hero-caption">There’s some thing funny about this wine</div>

<div class="abs main"></div>

<h1 class="abs title">The <em>Cork Lantern Radio</em></h1>
<div class="abs title-rule"></div>
<div class="abs feature-photo" role="img" aria-label="Glass of red wine and bottle over a golden vineyard at sunset"></div>
<p class="abs intro">Sed ut perspiciatis unde omnis iste natus error sit voluptatem accusantium doloremque laudaum, totam rem aperiam, eaque ipsa quae ab illo inventore veritatis et quasi architecto beatae vitae dicta sunt explicabo. Nemo enim ipsam voluptatem quia voluptas sit aspernatur aut odit aut fugit, sed quia consequuntur magni dolores eos qui ratione voluptatem sequi nesciunt. Neque porro quisquam est, qui dolorem ipsum quia dolor sit amet, consectetur, adipisci velit, sed quia non numquam eius modi tempora incidunt ut labore et dolore .</p>
<div class="abs like-row"><span class="like-btn">Tetszik</span><span class="like-sq"></span>3 ember kedveli. Legyél te az első az ismerőseid közül!</div>
<div class="abs tags">Címkék: <b>decima eodem parum quod</b></div>
<div class="abs rule" style="left:63px;top:718px;width:411px"></div>

<h2 class="abs h2" style="left:75px;top:742px">Lorem ipsum dolor sit amet</h2>
<ul class="abs bullets">
  <li>Sed ut perspiciatis unde omnis iste natus error sit</li>
  <li>voluptatem accusantium doloremque laudantium totam</li>
  <li>aperiam, eaque ipsa quae ab illo inventore</li>
  <li>veritatis et quasi architecto beatae vitae dicta sunt explicabo</li>
  <li>&nbsp;Nemo enim ipsam voluptatem quia voluptas</li>
</ul>
<div class="abs btn">Download Now</div>

<h3 class="abs sub" style="left:76px;top:917px">Sed ut perspiciatis</h3>
<p class="abs copy">perspiciatis unde omnis iste <a>natus error sit voluptatem</a> accusantium doloremque laudaum, totam rem aperiam, eaque ipsa quae ab illo inventore veritatis et quasi architecto beatae <a>vitae dicta sunt explicabo</a>.</p>
<div class="abs rule" style="left:63px;top:992px;width:411px"></div>

<h3 class="abs sub" style="left:78px;top:1003px">Uncorked</h3>
<article class="abs card">
  <div class="abs avatar" role="img" aria-label="Guest photo"></div>
  <div class="abs card-name">Lena</div>
  <div class="abs card-date">2014.06.09</div>
  <div class="abs card-rule"></div>
  <p class="abs card-text">This week on Cork Lantern Radio, host Owen Hartley speaks with two of the biggest experts on the growing popularity of wine in Asia.</p>
  <div class="abs card-more">View More</div>
</article>

<div class="abs rule foot-rule"></div>
<div class="abs foot" style="left:77px">(c) 2013 Cork Lantern Radio - All right reserve</div>
<div class="abs foot" style="right:77px">Home About Contact Us</div>

<aside>
  <section class="abs box" style="top:330px;height:152px">
    <div class="box-head">A BLOG</div><div class="box-rule"></div>
    <div class="box-art" role="img" aria-label="Engraving of a wine press"></div>
    <p class="blog-text">Lorem ipsum dolor sit amet, consectetuer adipiscing elit, sed diam nonummy nibh euismod tincidunt ut laoreet dolore magna aliquam erat volutpat. Ut wisi enim ad minim veniam, quis nostrud exerci tation ullamcorper suscipit lobortis nisl ut aliquip ex ea commodo consequat.</p>
  </section>

  <section class="abs box" style="top:498px;height:68px">
    <div class="box-head">search</div><div class="box-rule" style="width:105px"></div>
    <div class="box-art" role="img" aria-label="Engraving of winemaking equipment"></div>
    <div class="search-field"></div>
    <div class="search-btn"><svg width="11" height="11" viewBox="0 0 11 11"><circle cx="4.5" cy="4.5" r="3.2" fill="none" stroke="#6e1a2c" stroke-width="1.5"/><line x1="7" y1="7" x2="10" y2="10" stroke="#6e1a2c" stroke-width="2"/></svg></div>
  </section>

  <section class="abs fb">
    <div class="fb-title">Cork Lantern Radio <small>on friendwall</small></div>
    <div class="fb-like like-btn">Tetszik</div>
    <div class="fb-count">2,025 ember kedveli: Cork Lantern Radio</div>
    <div class="fans">
      <div class="fan"><i style="background:#c9a268"></i>Varga</div>
      <div class="fan"><i style="background:#5a5a66"></i>Mira</div>
      <div class="fan"><i style="background:#c8b8a8"></i>Lena</div>
      <div class="fan"><i style="background:#8a8a84"></i>Hanna</div>
      <div class="fan"><i style="background:#d8ccb0"></i>Pál</div>
      <div class="fan"><i style="background:#9a9aa6"></i>Pál</div>
      <div class="fan"><i style="background:#c8b088"></i>Imre</div>
      <div class="fan"><i style="background:#a89a90"></i>Toth</div>
      <div class="fan"><i style="background:#7a6050"></i>Dora</div>
      <div class="fan"><i style="background:#8a6048"></i>Toth</div>
    </div>
    <div class="fb-foot"><span class="like-sq"></span>Social module</div>
  </section>

  <section class="abs box" style="top:770px;height:138px">
    <div class="box-head">Archives</div><div class="box-rule"></div>
    <div class="box-art" role="img" aria-label="Engraving of a barrel and cellar worker"></div>
    <div class="archive">
      <span><b>2012 június</b> (17)</span><span><b>2011 december</b> (17)</span>
      <span><b>2012 május</b> (15)</span><span><b>2011 november</b> (15)</span>
      <span><b>2012 április</b> (16)</span><span><b>2011 október</b> (56)</span>
      <span><b>2012 március</b> (14)</span><span><b>2011 szeptember</b> (15)</span>
      <span><b>2012 február</b> (16)</span><span><b>2011 augusztus</b> (16)</span>
      <span><b>2012 január</b> (12)</span><span><b>2011 július</b> (16)</span>
    </div>
    <div class="more">Tovább...</div>
  </section>

  <section class="abs box" style="top:926px;height:162px">
    <div class="box-head">Episodes</div><div class="box-rule"></div>
    <div class="box-art" role="img" aria-label="Engraving of a wine press"></div>
    <div class="ep-title">The Inside Scoop on China's Extraoinary Growth and Passion for Wine</div>
    <p class="ep-text">This week on Cork Lantern Radio host Owen Hartley speaks with two of the big-gest experts on the growing popularity of wine in Asia.</p>
    <div class="watch">Watch Now <svg width="15" height="15" viewBox="0 0 15 15"><circle cx="7.5" cy="7.5" r="7.5" fill="#111"/><path d="M6 4.5 L10.5 7.5 L6 10.5Z" fill="#fff"/></svg></div>
  </section>
</aside>

</body>
</html>
```